Coffeeshop menu for filter tip

We want to have a cannabis (coffeeshop) menu in the size 25mm wide x 60mm wide. Some examples attached.

it must have the following text:
Menu

WEED p/g
Velotrine €16
Cinderfox €14
Tide Rambler €14
Marigolden €16
Grand Pelican €14
Copper Comet €14

HASH p/g
Baltic Ember €12
Harbor Velvet€11
Plum Rova €14
Dusk Maple €10

Target Market(s)

tourist in Amsterdam

Requirements
Nice to have
• cannabis sign leaf
• No Cigarettes allowed symbol

```html
<!DOCTYPE html>
<html lang="en">
<head>
<meta charset="utf-8">
<title>Cannabis Coffee Shop Menu</title>
<link rel="stylesheet" href="https://fonts.googleapis.com/css2?family=Montserrat:wght@500;600&family=Playfair+Display:ital,wght@0,400;0,700;1,900&display=swap">
<style>
  :root {
    --bg-deep: #020403;
    --ink: #ffffff;
    --price: #2f8a3c;
    --leaf-green: #22b024;
    --sign-red: #e0202a;
    --silver-light: #f4f4f4;
    --silver-dark: #6c6c6c;
  }
  html, body { margin: 0; padding: 0; overflow: hidden; }
  body { width: 1200px; height: 2879px; background: var(--bg-deep); }
  .menu {
    position: relative; width: 1200px; height: 2879px; overflow: hidden;
    color: var(--ink);
  }
  .foliage {
    position: absolute; inset: 0;
    background:
      radial-gradient(ellipse 700px 900px at 10% 15%, rgba(30,60,36,0.55), transparent 70%),
      radial-gradient(ellipse 600px 800px at 95% 45%, rgba(26,52,32,0.5), transparent 70%),
      radial-gradient(ellipse 700px 700px at 15% 70%, rgba(24,48,30,0.5), transparent 70%),
      radial-gradient(ellipse 800px 600px at 80% 95%, rgba(28,56,34,0.5), transparent 70%),
      var(--bg-deep);
  }
  .menu-heading {
    position: absolute; left: 60px; top: 52px; margin: 0;
    font-family: "Playfair Display", serif; font-weight: 400; font-size: 42px; line-height: 1;
    letter-spacing: 0.3em;
  }
  .icon { position: absolute; }
  .section-title {
    position: absolute; left: 0; width: 1200px; text-align: center;
    font-family: "Playfair Display", serif; font-weight: 700;
    font-size: 128px; line-height: 1; letter-spacing: 0.4em; text-indent: 0.4em;
    margin: 0;
  }
  .unit-label {
    position: absolute; left: 674px;
    font-family: "Montserrat", sans-serif; font-weight: 500; font-size: 30px; line-height: 1;
    color: var(--price); letter-spacing: 0.04em;
  }
  .price-list { position: absolute; left: 250px; border-left: 10px solid var(--ink); margin: 0; padding: 0; list-style: none; }
  .price-row {
    position: absolute; left: 40px; width: 600px; height: 47px;
    font-family: "Montserrat", sans-serif; font-weight: 600; font-size: 47px; line-height: 1;
    letter-spacing: 0.02em;
  }
  .price-row .price { position: absolute; left: 374px; color: var(--price); font-weight: 500; }
  .tagline {
    position: absolute; left: 0; width: 1200px; text-align: center;
    font-family: "Playfair Display", serif; font-weight: 400; font-size: 40px; line-height: 1;
    letter-spacing: 0.3em; text-indent: 0.3em;
  }
  .shop-name {
    position: absolute; left: 0; width: 1200px; text-align: center;
    font-family: "Playfair Display", serif; font-style: italic; font-weight: 900;
    font-size: 72px; line-height: 1; letter-spacing: 0.38em; text-indent: 0.38em;
    background: linear-gradient(180deg, var(--silver-light) 0%, var(--silver-light) 35%, var(--silver-dark) 100%);
    -webkit-background-clip: text; background-clip: text; color: transparent;
  }
  .divider { position: absolute; left: 132px; top: 1434px; width: 938px; height: 10px; background: var(--ink); }
</style>
</head>
<body>
<main class="menu">
  <div class="foliage" role="img" aria-label="Dark background of overlapping cannabis leaves"></div>

  <h1 class="menu-heading">Menu</h1>

  <svg class="icon leaf-icon" style="left:995px;top:42px" width="68" height="68" viewBox="0 0 100 100" aria-hidden="true">
    <g fill="var(--leaf-green)">
      <path d="M50 8 C58 30 58 55 50 75 C42 55 42 30 50 8Z"/>
      <path d="M50 75 C62 52 78 38 96 32 C88 50 72 66 50 75Z"/>
      <path d="M50 75 C38 52 22 38 4 32 C12 50 28 66 50 75Z"/>
      <path d="M50 75 C66 68 82 68 96 74 C82 82 66 82 50 75Z"/>
      <path d="M50 75 C34 68 18 68 4 74 C18 82 34 82 50 75Z"/>
      <rect x="48" y="74" width="4" height="20"/>
    </g>
  </svg>
  <svg class="icon no-smoking" style="left:1091px;top:40px" width="72" height="72" viewBox="0 0 100 100" aria-hidden="true">
    <circle cx="50" cy="50" r="42" fill="#fff" stroke="var(--sign-red)" stroke-width="12"/>
    <rect x="20" y="46" width="52" height="12" fill="#111"/>
    <rect x="74" y="46" width="6" height="12" fill="#111"/>
    <line x1="22" y1="22" x2="78" y2="78" stroke="var(--sign-red)" stroke-width="12"/>
  </svg>
  <h2 class="section-title" style="top:112px">WEED</h2>
  <div class="unit-label" style="top:412px">p/g</div>
  <ul class="price-list" style="top:477px;height:462px">
    <li class="price-row" style="top:-2px">Velotrine<span class="price">€16</span></li>
    <li class="price-row" style="top:82px">Cinderfox<span class="price">€14</span></li>
    <li class="price-row" style="top:166px">Tide Rambler<span class="price">€14</span></li>
    <li class="price-row" style="top:250px">Marigolden<span class="price">€16</span></li>
    <li class="price-row" style="top:334px">Grand Pelican<span class="price">€14</span></li>
    <li class="price-row" style="top:418px">Copper Comet<span class="price">€14</span></li>
  </ul>
  <div class="tagline" style="top:1191px">cannabis</div>
  <div class="shop-name" style="top:1264px">COFFEE SHOP</div>

  <div class="divider"></div>

  <svg class="icon leaf-icon" style="left:995px;top:1486px" width="68" height="68" viewBox="0 0 100 100" aria-hidden="true">
    <g fill="var(--leaf-green)">
      <path d="M50 8 C58 30 58 55 50 75 C42 55 42 30 50 8Z"/>
      <path d="M50 75 C62 52 78 38 96 32 C88 50 72 66 50 75Z"/>
      <path d="M50 75 C38 52 22 38 4 32 C12 50 28 66 50 75Z"/>
      <path d="M50 75 C66 68 82 68 96 74 C82 82 66 82 50 75Z"/>
      <path d="M50 75 C34 68 18 68 4 74 C18 82 34 82 50 75Z"/>
      <rect x="48" y="74" width="4" height="20"/>
    </g>
  </svg>
  <svg class="icon no-smoking" style="left:1091px;top:1484px" width="72" height="72" viewBox="0 0 100 100" aria-hidden="true">
    <circle cx="50" cy="50" r="42" fill="#fff" stroke="var(--sign-red)" stroke-width="12"/>
    <rect x="20" y="46" width="52" height="12" fill="#111"/>
    <rect x="74" y="46" width="6" height="12" fill="#111"/>
    <line x1="22" y1="22" x2="78" y2="78" stroke="var(--sign-red)" stroke-width="12"/>
  </svg>
  <h2 class="section-title" style="top:1560px">HASH</h2>
  <div class="unit-label" style="top:1834px">p/g</div>
  <ul class="price-list" style="top:1899px;height:296px">
    <li class="price-row" style="top:-1px">Baltic Ember<span class="price">€12</span></li>
    <li class="price-row" style="top:82px">Harbor Velvet<span class="price">€11</span></li>
    <li class="price-row" style="top:166px">Plum Rova<span class="price">€14</span></li>
    <li class="price-row" style="top:251px">Dusk Maple<span class="price">€10</span></li>
  </ul>
  <div class="tagline" style="top:2633px">cannabis</div>
  <div class="shop-name" style="top:2706px">COFFEE SHOP</div>
</main>
</body>
</html>
```